Need stationery and business card design for Appraisal Company
Stonewell Valuations & Advisory
Professional
Lonny Harwick
Certified Residential Appraiser
5182 W Maple Ct.
Larkfield, AZ 85299
lonny@stonewellvaluations.example
Business logo and font will be uploaded.

```html
<!DOCTYPE html>
<html lang="en">
<head>
<meta charset="utf-8">
<title>Stonewell Valuations &amp; Advisory — Business Card</title>
<link rel="stylesheet" href="https://fonts.googleapis.com/css2?family=Cinzel:wght@400;600&display=swap">
<style>
  :root {
    --page-bg: #e9e6e2;
    --card-white: #ffffff;
    --card-shade: #eeeeee;
    --brand-red: #e2301f;
    --brand-red-dark: #b81d10;
    --ink-dark: #3a3a3a;
    --ink-grey: #6b6b6b;
    --rule-grey: #d4d4d4;
  }
  * { box-sizing: border-box; margin: 0; padding: 0; }
  html, body {
    width: 1200px; height: 900px; overflow: hidden;
    background: var(--page-bg);
    font-family: "Cinzel", serif;
  }
  .business-card {
    position: absolute; left: 110px; top: 170px;
    width: 980px; height: 560px;
    background: radial-gradient(ellipse at 40% 40%, var(--card-white) 55%, var(--card-shade) 100%);
    box-shadow: 0 18px 40px rgba(0,0,0,0.25);
    overflow: hidden;
  }
  .side-band {
    position: absolute; right: 0; top: 0;
    width: 64px; height: 100%;
    background: linear-gradient(to right, var(--brand-red-dark), var(--brand-red));
    display: flex; justify-content: center;
  }
  .side-band__url {
    margin-top: 28px;
    writing-mode: vertical-rl;
    color: var(--card-white); font-size: 15px; letter-spacing: 1.5px;
    white-space: nowrap;
  }
  .company-name {
    position: absolute; left: 120px; top: 92px;
    display: flex; align-items: center; gap: 22px;
  }
  .company-name__mark {
    flex: none; width: 46px; height: 46px; background: var(--brand-red);
  }
  .company-name__text {
    color: var(--ink-dark); font-weight: 600; font-size: 38px; letter-spacing: 2px;
    line-height: 1.05;
  }
  .person {
    position: absolute; left: 78px; top: 292px;
  }
  .person__pointer {
    position: absolute; left: -78px; top: 6px;
    width: 0; height: 0;
    border-top: 13px solid transparent; border-bottom: 13px solid transparent;
    border-left: 18px solid var(--brand-red);
  }
  .person__name { color: var(--brand-red); font-size: 25px; font-weight: 600; letter-spacing: 1px; }
  .person__title { color: var(--ink-grey); font-size: 19px; font-weight: 400; margin-top: 6px; letter-spacing: 0.5px; }
  .divider {
    position: absolute; left: 465px; top: 280px;
    width: 1px; height: 170px; background: var(--rule-grey);
  }
  .contact-list {
    position: absolute; left: 485px; top: 282px;
    list-style: none; color: var(--ink-grey); font-size: 17px; letter-spacing: 0.4px;
    white-space: nowrap;
  }
  .contact-list__item { display: flex; align-items: flex-start; gap: 12px; line-height: 26px; margin-bottom: 4px; }
  .contact-list__icon { flex: none; width: 20px; height: 20px; margin-top: 3px; }
  .contact-list__lines { display: flex; flex-direction: column; }
</style>
</head>
<body>
  <main class="business-card">
    <div class="company-name">
      <div class="company-name__mark"></div>
      <div class="company-name__text">Stonewell Valuations<br>&amp; Advisory</div>
    </div>

    <section class="person">
      <span class="person__pointer"></span>
      <h1 class="person__name">Lonny Harwick</h1>
      <p class="person__title">Certified Residential Appraiser</p>
    </section>

    <div class="divider"></div>

    <ul class="contact-list">
      <li class="contact-list__item">
        <svg class="contact-list__icon" viewBox="0 0 20 20"><circle cx="10" cy="10" r="10" fill="#e2301f"/><path d="M5 10.5 10 6l5 4.5M6.5 9.5V14h7V9.5" fill="none" stroke="#fff" stroke-width="1.4"/></svg>
        <span class="contact-list__lines"><span>5182 W Maple Ct.</span><span>Larkfield, AZ 85299</span></span>
      </li>
      <li class="contact-list__item">
        <svg class="contact-list__icon" viewBox="0 0 20 20"><circle cx="10" cy="10" r="10" fill="#e2301f"/><path d="M7 5.5h2l1 2.5-1.3 1a6 6 0 0 0 2.3 2.3l1-1.3 2.5 1v2a1 1 0 0 1-1 1A8.5 8.5 0 0 1 6 6.5a1 1 0 0 1 1-1z" fill="#fff"/></svg>
        <span>602-555-0148</span>
      </li>
      <li class="contact-list__item">
        <svg class="contact-list__icon" viewBox="0 0 20 20"><circle cx="10" cy="10" r="10" fill="#e2301f"/><rect x="5" y="6.5" width="10" height="7" fill="none" stroke="#fff" stroke-width="1.3"/><path d="M5 6.5l5 4 5-4" fill="none" stroke="#fff" stroke-width="1.3"/></svg>
        <span>lonny@stonewellvaluations.example</span>
      </li>
      <li class="contact-list__item">
        <svg class="contact-list__icon" viewBox="0 0 20 20"><circle cx="10" cy="10" r="10" fill="#e2301f"/><circle cx="10" cy="10" r="5" fill="none" stroke="#fff" stroke-width="1.2"/><path d="M5 10h10M10 5c-2.5 3-2.5 7 0 10M10 5c2.5 3 2.5 7 0 10" fill="none" stroke="#fff" stroke-width="1"/></svg>
        <span>www.StonewellValuations.example</span>
      </li>
    </ul>

    <aside class="side-band">
      <span class="side-band__url">www.stonewellvaluations.example</span>
    </aside>
  </main>
</body>
</html>
```